Design A Responsive Website for Our Bar/Event Center and Restaurant

We need a Responsive Word Press Website for our Bar Event Center and our Restaurant. We need 5 pages with one page being our menu with the ability for customers to place online orders for food.
We need the entire website designed, coded and deployed. We have domain names already that need to link to the website and we also have hosting so we need the website deployed at our hosting provider. Pages should include 1) About Us 2)Bar 3)Restaurant-Menus 4) Event Venue-With Calendar 5) Contact Us

Target Market(s)

Adults 21-75 in the Louisville KY area, that go to bars, night clubs, concerts and karaoke events

Industry/Entity Type

Bar-Night Club-Music- Events

Coding

Coded - Design and coding required

Number of Pages Required

5+ page

Other font styles liked:
• Use a Font like in our logos

Colors
EE7325
F08F49
F5BC92
FAE3D3
FDF4ED
EB3D1F
EC4F4E
F09395
F8D3D4
FCEDEE

Requirements
Must have
• Online Menu Ordering with Shopping Cart, An Updateable Event Calendar, A page for posting past event pictures and videos, Ability to sell Event tickets
Nice to have
• Ability to live stream events to facebook
Should not have
• NA

```html
<!DOCTYPE html>
<html lang="en">
<head>
<meta charset="utf-8">
<title>Hilltop Tavern Bar and Event Center</title>
<link href="https://fonts.googleapis.com/css2?family=Lilita+One&family=Roboto:wght@400;500;700&display=swap" rel="stylesheet">
<style>
:root{
  --orange:#EE7325;
  --orange-light:#F08F49;
  --orange-dark:#C9581A;
  --red:#EC4F4E;
  --red-deep:#EB3D1F;
  --black:#000;
  --ink:#05090b;
  --footer:#0b0b0b;
  --white:#fff;
  --muted:#e6e6e6;
}
*{margin:0;padding:0;box-sizing:border-box}
html,body{width:1200px;height:3428px;overflow:hidden;background:var(--black)}
body{font-family:"Roboto",sans-serif;color:var(--white);position:relative}
.abs{position:absolute}
.heading{font-family:"Lilita One",sans-serif;color:var(--orange);letter-spacing:.5px;text-transform:uppercase}
.btn{position:absolute;display:flex;align-items:center;justify-content:center;border-radius:22px;color:var(--white);font-size:14px;font-weight:500;text-transform:uppercase}
.btn-orange{background:var(--orange)}
.btn-red{background:var(--red)}
.photo{position:absolute}

/* top bar */
.topbar{top:0;left:0;width:1200px;height:90px;background:var(--black);border-top:2px solid var(--orange)}
.brand{left:112px;top:4px;width:190px;height:73px;background:#111;display:flex;align-items:center;justify-content:center;gap:8px}
.brand-dot{width:12px;height:12px;border-radius:50%;background:var(--orange)}
.brand-name{font-family:"Roboto",sans-serif;font-weight:700;font-size:19px;color:var(--orange)}
.contact-chip{display:flex;align-items:center;gap:10px;font-size:15px;font-weight:500;top:25px}
.chip-icon{width:34px;height:34px;border-radius:50%;background:var(--orange);display:flex;align-items:center;justify-content:center}

/* nav */
.nav{top:90px;left:0;width:1200px;height:56px;background:var(--orange)}
.nav-item{position:absolute;top:0;height:56px;line-height:56px;font-size:15px;text-transform:uppercase;color:var(--white)}
.nav-home{left:112px;width:118px;text-align:center;background:var(--orange-dark)}
.nav-sep{position:absolute;top:0;line-height:56px;font-size:14px}
.wave{position:absolute;left:0;width:1200px;height:10px}

/* hero */
.hero{top:146px;left:0;width:1200px;height:635px;background:linear-gradient(100deg,#2a1d12 0%,#5a3b22 35%,#8b6a4e 60%,#3a3a40 100%)}
.hero-disc{left:95px;top:80px;width:440px;height:440px;border-radius:50%;background:rgba(10,8,6,.55)}
.hero-text{left:115px;width:400px;text-align:center}

/* about */
.about{top:781px;left:0;width:1200px;height:587px;background:var(--black)}
.about p{font-size:15px;line-height:25.7px;text-align:justify;color:var(--white)}

/* bar menus */
.bar{top:1368px;left:0;width:1200px;height:521px;background:var(--ink)}
.drink{position:absolute;top:157px;width:240px;text-align:center}
.drink-circle{width:160px;height:160px;border-radius:50%;margin:0 auto}
.drink h4{font-size:13px;font-weight:700;margin-top:29px}
.drink p{font-size:12px;line-height:20px;margin-top:13px;color:var(--muted)}

/* restaurant */
.dish{position:absolute;top:2043px;width:304px}
.dish-photo{height:234px}
.dish h4{text-align:center;font-size:15px;font-weight:700;margin-top:27px}

/* events */
.card{position:absolute;border:1px solid #3a3a3a;border-radius:6px;background:#050505}
.event-title{font-size:16px;font-weight:700}
.meta{display:flex;align-items:center;gap:6px;font-size:13.5px;color:var(--orange);font-weight:500}
.event-text{font-size:13.5px;line-height:22px;color:var(--white)}
.read{font-size:13px;color:var(--orange);text-decoration:underline;font-weight:500}

/* footer */
.footer{top:3026px;left:0;width:1200px;height:340px;background:var(--footer)}
.foot-head{font-size:17px;font-weight:700;text-transform:uppercase}
.foot-list{list-style:none;font-size:15px}
.foot-list li{height:34.5px;display:flex;align-items:center;gap:12px}
.social{position:absolute;top:3179px;width:32px;height:32px;border:1.5px solid var(--white);border-radius:50%}
.copy{top:3366px;left:0;width:1200px;height:62px;background:var(--orange);text-align:center;font-size:13.5px;line-height:70px}
</style>
</head>
<body>

<!-- top bar -->
<header class="abs topbar">
  <div class="abs brand"><span class="brand-dot"></span><span class="brand-name">Hilltop Tavern</span></div>
  <div class="abs contact-chip" style="left:340px">
    <span class="chip-icon"><svg width="16" height="16" viewBox="0 0 24 24" fill="#fff"><path d="M6.6 10.8a15.1 15.1 0 0 0 6.6 6.6l2.2-2.2a1 1 0 0 1 1-.25 11.4 11.4 0 0 0 3.6.57 1 1 0 0 1 1 1V20a1 1 0 0 1-1 1A17 17 0 0 1 3 4a1 1 0 0 1 1-1h3.5a1 1 0 0 1 1 1c0 1.25.2 2.45.57 3.57a1 1 0 0 1-.25 1z"/></svg></span>502-555-0148</div>
  <div class="abs contact-chip" style="left:505px;top:22px">
    <span class="chip-icon"><svg width="16" height="16" viewBox="0 0 24 24" fill="none" stroke="#fff" stroke-width="2"><rect x="3" y="5" width="18" height="14" rx="2"/><path d="M3 7l9 6 9-6"/></svg></span><span style="margin-top:-8px">orders@hilltoptavern.example</span></div>
  <div class="btn btn-orange" style="left:765px;top:23px;width:157px;height:40px">Order Online</div>
  <div class="btn btn-red" style="left:930px;top:23px;width:157px;height:40px">Event Tickets</div>
</header>

<!-- navigation -->
<nav class="abs nav">
  <span class="nav-item nav-home">Home</span>
  <span class="nav-item" style="left:262px">About Us</span>
  <span class="nav-sep" style="left:364px">|</span>
  <span class="nav-item" style="left:403px">Bar</span>
  <span class="nav-sep" style="left:470px">|</span>
  <span class="nav-item" style="left:504px">Restaurant-Menus</span>
  <span class="nav-sep" style="left:682px">|</span>
  <span class="nav-item" style="left:720px">Event</span>
  <span class="nav-sep" style="left:802px">|</span>
  <span class="nav-item" style="left:835px">Contact Us</span>
  <span class="nav-item" style="left:1019px;font-weight:700;display:flex;align-items:center;gap:6px">Login
    <svg width="12" height="13" viewBox="0 0 12 13" fill="#fff"><rect x="1" y="6" width="10" height="7" rx="1"/><path d="M3 6V4a3 3 0 0 1 6 0v2" fill="none" stroke="#fff" stroke-width="1.6"/></svg></span>
</nav>

<!-- hero -->
<section class="abs hero" role="img" aria-label="Photo of a smiling couple sharing food at a restaurant table">
  <div class="abs hero-disc"></div>
  <div class="abs hero-text" style="top:194px"><div class="heading" style="font-family:Roboto,sans-serif;font-weight:700;font-size:23px">Welcome To</div></div>
  <div class="abs hero-text heading" style="top:238px;font-size:29px;line-height:34px">Hilltop Tavern Bar<br>and Event Center</div>
  <div class="abs hero-text" style="left:115px;width:400px;top:315px;font-size:15px;line-height:26px">Lorem ipsum dolor sit amet consectetur adipiscing elit, sed do eiusmod tempor incididunt ut labore et dolore</div>
  <div class="btn btn-red" style="left:237px;top:383px;width:157px;height:41px">Get Started</div>
</section>
<svg class="wave" style="top:144px" viewBox="0 0 1200 10" preserveAspectRatio="none"><path d="M0 0H1200V2Q1190 10 1180 2T1160 2T1140 2T1120 2T1100 2T1080 2T1060 2T1040 2T1020 2T1000 2T980 2T960 2T940 2T920 2T900 2T880 2T860 2T840 2T820 2T800 2T780 2T760 2T740 2T720 2T700 2T680 2T660 2T640 2T620 2T600 2T580 2T560 2T540 2T520 2T500 2T480 2T460 2T440 2T420 2T400 2T380 2T360 2T340 2T320 2T300 2T280 2T260 2T240 2T220 2T200 2T180 2T160 2T140 2T120 2T100 2T80 2T60 2T40 2T20 2T0 2Z" fill="#EE7325"/></svg>

<!-- about -->
<section class="abs about">
  <div class="photo" style="left:206px;top:95px;width:310px;height:394px;background:linear-gradient(160deg,#6b4a35,#b98a62 55%,#4a3428)" role="img" aria-label="Photo of hands passing plates of salad across a wooden table"></div>
  <div class="photo" style="left:68px;top:147px;width:227px;height:256px;background:linear-gradient(170deg,#3b3550,#7a5a48 45%,#2e2520)" role="img" aria-label="Photo of friends toasting drinks on a rooftop at dusk"></div>
  <div class="abs" style="left:169px;top:263px;width:24px;height:24px;border-radius:50%;background:#fff;display:flex;align-items:center;justify-content:center"><svg width="10" height="10" viewBox="0 0 10 10"><path d="M2 1L9 5L2 9Z" fill="#222"/></svg></div>
  <div class="photo" style="left:446px;top:352px;width:130px;height:120px;background:linear-gradient(160deg,#6b4a30,#c7955c,#3d4a66)" role="img" aria-label="Photo of diners laughing at a restaurant table"></div>
  <h2 class="abs heading" style="left:617px;top:75px;font-size:35px">About Us</h2>
  <p class="abs" style="left:617px;top:128px;width:490px">Hilltop Tavern Bar and Event Center is exactly that. It’s a bar / night club in Louisville, Kentucky’s south end located at 4120 Maple Ridge Road, off the Ridgeway Parkway. Easily accessible 2 minutes from the end of the Outer Loop Freeway, Hilltop is your favorite neighborhood bar that you’ve never been to. Our crowd welcomes everyone but tends to lean to ages 30 and up. With our “old neighborhood pub” like atmosphere, you will find that everyone knows your name. Hilltop has 5000 sq/ft of indoor space in two separate suites each able to accommodate100 guests. Come in to Hilltop to enjoy our great bar food menu featuring appetizers, burgers, brats and wraps or order from Hilltop Wing Hour – our 24 Sauce Wing Buffet open 11am-7pm Monday-Friday! After you finish dinner, enjoy a beer or a cocktail while listening to a band or sing karaoke.</p>
  <div class="btn btn-orange" style="left:617px;top:460px;width:158px;height:41px">Learn More</div>
  <div class="btn btn-red" style="left:782px;top:460px;width:158px;height:41px">Calendar</div>
</section>

<!-- bar menus -->
<section class="abs bar">
  <h2 class="abs heading" style="left:0;width:1200px;text-align:center;top:76px;font-size:35px">Bar Menus</h2>
  <div class="drink" style="left:94px"><div class="drink-circle" style="background:radial-gradient(circle at 50% 60%,#e0843a,#b23a45 55%,#2a1a14)" role="img" aria-label="Photo of colourful fruit cocktails"></div><h4>LOREM IPSUM DOLOR SIT</h4><p>Loremt ipsum dolor amed consectetur<br>adipiscing sed do eiusmod tempor.</p></div>
  <div class="drink" style="left:351px"><div class="drink-circle" style="background:radial-gradient(circle at 50% 60%,#e8a234,#6a4a28 55%,#1c1612)" role="img" aria-label="Photo of a glass of draft beer"></div><h4>LOREM IPSUM DOLOR SIT</h4><p>Loremt ipsum dolor amed consectetur<br>adipiscing sed do eiusmod tempor.</p></div>
  <div class="drink" style="left:608px"><div class="drink-circle" style="border:1.5px solid var(--orange);background:radial-gradient(circle at 50% 55%,#d8dcc0,#5a4a30 45%,#150f0a)" role="img" aria-label="Photo of a tall cocktail with mint"></div><h4>LOREM IPSUM DOLOR SIT</h4><p>Loremt ipsum dolor amed consectetur<br>adipiscing sed do eiusmod tempor.</p></div>
  <div class="drink" style="left:864px"><div class="drink-circle" style="background:radial-gradient(circle at 50% 60%,#d0405a,#6a3a3a 50%,#1a1616)" role="img" aria-label="Photo of a red cocktail and a martini glass"></div><h4>LOREM IPSUM DOLOR SIT</h4><p>Loremt ipsum dolor amed consectetur<br>adipiscing sed do eiusmod tempor.</p></div>
</section>

<!-- restaurant menus -->
<h2 class="abs heading" style="left:0;width:1200px;text-align:center;top:1966px;font-size:35px">Restaurant-Menus</h2>
<div class="dish" style="left:112px"><div class="dish-photo" style="background:radial-gradient(circle at 50% 60%,#5d8a3a,#23261f 55%,#111)" role="img" aria-label="Photo of a steaming bowl of vegetables"></div><h4>LOREM IPSUM DOLOR SIT AMETED</h4></div>
<div class="dish" style="left:447px"><div class="dish-photo" style="background:radial-gradient(circle at 50% 55%,#c0823a,#4a3a34 55%,#2a2a2e)" role="img" aria-label="Photo of a cheeseburger"></div><h4>LOREM IPSUM DOLOR SIT AMETED</h4></div>
<div class="dish" style="left:785px"><div class="dish-photo" style="background:radial-gradient(circle at 45% 65%,#e8d8c0,#9a5a34 45%,#3a1c10)" role="img" aria-label="Photo of a plated dish with wine on a restaurant table"></div><h4>LOREM IPSUM DOLOR SIT AMETED</h4></div>

<!-- events -->
<h2 class="abs heading" style="left:0;width:1200px;text-align:center;top:2397px;font-size:35px">Our Events</h2>
<div class="card" style="left:112px;top:2487px;width:444px;height:452px">
  <div class="abs" style="left:7px;top:8px;width:429px;height:291px;background:linear-gradient(160deg,#4a3a34,#b4806a 50%,#5a3a2e)" role="img" aria-label="Photo of friends sharing dinner at a table"></div>
  <div class="abs event-title" style="left:23px;top:320px">Lorem ipsum dolor sit ameted consectetur</div>
  <div class="abs meta" style="left:23px;top:354px"><svg width="13" height="13" viewBox="0 0 13 13" fill="#EE7325"><rect x="1" y="2" width="11" height="10" rx="1"/><rect x="2.5" y="5" width="8" height="5.5" fill="#050505"/></svg>Oct 2022 &nbsp;|&nbsp; <svg width="12" height="13" viewBox="0 0 12 13" fill="none" stroke="#EE7325" stroke-width="1.4"><circle cx="6" cy="4" r="3"/><path d="M1 12c0-3 2-4.5 5-4.5s5 1.5 5 4.5"/></svg> John Doe</div>
  <div class="abs event-text" style="left:23px;top:384px;width:400px">Lorem ipsum dolor sit amet, consectetur adipiscing elit, sed do eiusmod tempor incididunt ut labore et dolore magnad.</div>
</div>
<div class="card" style="left:579px;top:2487px;width:502px;height:220px">
  <div class="abs" style="left:9px;top:10px;width:185px;height:198px;background:linear-gradient(160deg,#3a2a1a,#b07a40 50%,#4a3020)" role="img" aria-label="Photo of friends raising beers in a pub"></div>
  <div class="abs event-title" style="left:219px;top:33px">Lorem ipsum dolor sit onsectetur</div>
  <div class="abs meta" style="left:219px;top:66px"><svg width="13" height="13" viewBox="0 0 13 13" fill="#EE7325"><rect x="1" y="2" width="11" height="10" rx="1"/><rect x="2.5" y="5" width="8" height="5.5" fill="#050505"/></svg>Oct 2022 &nbsp;|&nbsp; <svg width="12" height="13" viewBox="0 0 12 13" fill="none" stroke="#EE7325" stroke-width="1.4"><circle cx="6" cy="4" r="3"/><path d="M1 12c0-3 2-4.5 5-4.5s5 1.5 5 4.5"/></svg> John Doe</div>
  <div class="abs event-text" style="left:219px;top:91px;width:270px">Lorem ipsum dolor sit amet, consectetur adipiscing elited sed do eiusmod tempor incididunt labore dolore magnad Uted.</div>
  <div class="abs read" style="left:219px;top:170px">Read More</div>
</div>
<div class="card" style="left:579px;top:2719px;width:502px;height:220px">
  <div class="abs" style="left:9px;top:10px;width:185px;height:198px;background:linear-gradient(160deg,#3a2418,#a86a40 50%,#3a3a50)" role="img" aria-label="Photo of a couple chatting over dinner"></div>
  <div class="abs event-title" style="left:219px;top:33px;color:var(--orange)">Lorem ipsum dolor sit onsectetur</div>
  <div class="abs meta" style="left:219px;top:66px"><svg width="13" height="13" viewBox="0 0 13 13" fill="#EE7325"><rect x="1" y="2" width="11" height="10" rx="1"/><rect x="2.5" y="5" width="8" height="5.5" fill="#050505"/></svg>Oct 2022 &nbsp;|&nbsp; <svg width="12" height="13" viewBox="0 0 12 13" fill="none" stroke="#EE7325" stroke-width="1.4"><circle cx="6" cy="4" r="3"/><path d="M1 12c0-3 2-4.5 5-4.5s5 1.5 5 4.5"/></svg> John Doe</div>
  <div class="abs event-text" style="left:219px;top:91px;width:270px">Lorem ipsum dolor sit amet, consectetur adipiscing elited sed do eiusmod tempor incididunt labore dolore magnad Uted.</div>
  <div class="abs read" style="left:219px;top:170px">Read More</div>
</div>

<!-- footer -->
<footer class="abs footer">
  <div class="abs" style="left:98px;top:75px;display:flex;align-items:center;gap:8px"><span class="brand-dot"></span><span class="brand-name" style="font-size:24px">Hilltop Tavern</span></div>
  <div class="abs foot-head" style="left:401px;top:66px">Hours</div>
  <ul class="abs foot-list" style="left:398px;top:94px">
    <li><span>&raquo;</span>Monday-Thursday</li>
    <li style="padding-left:23px">11am-11pm (or later!)</li>
    <li><span>&raquo;</span>Friday &amp; Saturday</li>
    <li style="padding-left:23px">11am-3am</li>
    <li><span>&raquo;</span>Sunday Noon</li>
    <li style="padding-left:23px">11pm (or later!)</li>
  </ul>
  <div class="abs foot-head" style="left:647px;top:66px">Quick Links</div>
  <ul class="abs foot-list" style="left:647px;top:95px">
    <li><span>&raquo;</span>Home</li><li><span>&raquo;</span>About Us</li><li><span>&raquo;</span>Bar</li>
    <li><span>&raquo;</span>Restaurant-Menus</li><li><span>&raquo;</span>Event</li><li><span>&raquo;</span>Contact Us</li>
  </ul>
  <div class="abs foot-head" style="left:883px;top:66px">Contact Us</div>
  <svg class="abs" style="left:885px;top:113px" width="14" height="14" viewBox="0 0 24 24" fill="#fff"><path d="M6.6 10.8a15.1 15.1 0 0 0 6.6 6.6l2.2-2.2a1 1 0 0 1 1-.25 11.4 11.4 0 0 0 3.6.57 1 1 0 0 1 1 1V20a1 1 0 0 1-1 1A17 17 0 0 1 3 4a1 1 0 0 1 1-1h3.5a1 1 0 0 1 1 1c0 1.25.2 2.45.57 3.57a1 1 0 0 1-.25 1z"/></svg>
  <div class="abs" style="left:913px;top:111px;font-size:12px;font-weight:700">Phone</div>
  <div class="abs" style="left:913px;top:134px;font-size:15px">502-555-0148</div>
  <svg class="abs" style="left:884px;top:176px" width="16" height="13" viewBox="0 0 16 13" fill="#fff"><rect width="16" height="13" rx="1.5"/><path d="M1 2l7 5 7-5" fill="none" stroke="#0b0b0b" stroke-width="1.5"/></svg>
  <div class="abs" style="left:913px;top:174px;font-size:12px;font-weight:700">Email</div>
  <div class="abs" style="left:913px;top:197px;font-size:15px">orders@hilltoptavern.example</div>
  <svg class="abs" style="left:886px;top:234px" width="11" height="15" viewBox="0 0 11 15" fill="#fff"><path d="M5.5 0A5.5 5.5 0 0 0 0 5.5C0 9.5 5.5 15 5.5 15S11 9.5 11 5.5A5.5 5.5 0 0 0 5.5 0z"/><circle cx="5.5" cy="5.5" r="2" fill="#0b0b0b"/></svg>
  <div class="abs" style="left:913px;top:233px;font-size:12px;font-weight:700">Location</div>
  <div class="abs" style="left:913px;top:256px;font-size:15px;line-height:23px">4120 Maple Ridge Road<br>Louisville, KY 40299</div>
</footer>
<span class="social" style="left:129px"></span>
<span class="social" style="left:170px"></span>
<span class="social" style="left:210px"></span>
<span class="social" style="left:250px"></span>

<div class="abs copy">2022 Copyright - Hilltop Tavern | All Rights Reserved</div>
<svg class="wave" style="top:3360px" viewBox="0 0 1200 10" preserveAspectRatio="none"><path d="M0 10H1200V8Q1190 0 1180 8T1160 8T1140 8T1120 8T1100 8T1080 8T1060 8T1040 8T1020 8T1000 8T980 8T960 8T940 8T920 8T900 8T880 8T860 8T840 8T820 8T800 8T780 8T760 8T740 8T720 8T700 8T680 8T660 8T640 8T620 8T600 8T580 8T560 8T540 8T520 8T500 8T480 8T460 8T440 8T420 8T400 8T380 8T360 8T340 8T320 8T300 8T280 8T260 8T240 8T220 8T200 8T180 8T160 8T140 8T120 8T100 8T80 8T60 8T40 8T20 8T0 8Z" fill="#EE7325"/></svg>

</body>
</html>
```